Cloud-based Health 2.0 Web Site

We need the overall look and feel for a new cloud-based Health 2.0 web site where health professionals can manage and interact with their patients/clients.

The plan is to generate a landing page that can grab the attention of health professionals (doctors, nurses, personal trainers, etc...). This page should have an attractive "Sign Up for Free" or similar button/message, as well as a login section for users already registered. We currently have a view on having a number of messages displayed, either as a slider or as separate areas on the page (decision is up for grabs).

Secondly, we need a standard "framework" for all the other pages which will be accessible once the user has authenticated with a clean, airy and spacious feel. This will provide styling for standard elements (input boxes, checkboxes, etc...) as well as a given layout, possibly 3 columns (fixed-fluid-fixed) although we leave this to the designer's choice.

We want to stress the importance of the Cloud, as well as make users feel like "this is the place to be if you're a modern, tech savvy health professional". Also of high importance is to show that this is a secure place, where data is accessible from anywhere yet also highly protected.

This project is going to provide long-term work for the winner and possibly those we consider close runner ups, so if you guys are interested in grabbing our attention so you can become our designer of choice, this is your chance!

Standard pages we are looking to receive after the selection process:

* Landing page
* Health Professional Profile Page (personal details, professional details, photo...)
* Patient list / Patient Management page
* Patient profile (details, health details...)
* Generic "item" management page (item refers to documents, images, contacts, etc...)

The logo for the site/product is also up for grabs, and a bonus payment can be given if you provide one that both matches the style of the site whilst being one that could be reused for mobile app icons, etc...

The site name is "vornatik" (all lower-case) for those of you wanting to work on the logo part. As I said before, the logo should contain a component that could be use as the recognisable icon in a mobile phone app. Something that can be easily identified in both the site and the app that connects them together.

vornatik is made up of two parts (vorn + atik), and you might want to consider differentiating them by the use of colour, fonts or however you think appropriate.

New sample screen-shots of the existing functionality have been uploaded to help you mock up some screens.

PLEASE NOTE: This are to be used for content/widget design only! The layout of how these are represented, e.g. accordion, slider, tree, list... is entirely up to you! Don't guide your layout based on these screen-shots, unless you think they are the way to go, of course. 

We want your creative input, so please innovate! :)

Thanks!

Target Market(s)

Health Professionals

Industry/Entity Type

Health

Requirements
Must have
• * A landing page that grabs the users attention but is "different" from the rest of pages (although within the same design/style parameters)

* A generic page framework for the rest of the pages (style guide)
Nice to have
• A modern and clean logo to go with the site. If the logo is selected, this can result in a bonus payment to be decided.

```html
<!DOCTYPE html>
<html lang="en">
<head>
<meta charset="utf-8">
<title>vornatik – Dashboard</title>
<link rel="stylesheet" href="https://fonts.googleapis.com/css2?family=Source+Sans+3:wght@400;600;700&family=Arimo:wght@400;700&display=swap">
<style>
  :root{
    --sky-top:#8fc6ea;
    --sky-mid:#c8e3f5;
    --sky-low:#eef6fc;
    --white:#ffffff;
    --panel-border:#dfe5ea;
    --brand-blue:#16a2e0;
    --side-top:#12a0e0;
    --side-bottom:#07478f;
    --text-dark:#222a30;
    --text-body:#4a4f54;
    --card-bg:#f4f4f4;
    --card-border:#dcdcdc;
    --footer-top:#7a7a7a;
    --footer-bottom:#3e3e3e;
    --submit-top:#9ad21e;
    --submit-bottom:#5b8d10;
  }
  *{box-sizing:border-box;margin:0;padding:0}
  html,body{width:1200px;height:864px;overflow:hidden}
  body{
    position:relative;
    font-family:"Source Sans 3",sans-serif;
    color:var(--text-dark);
    background:linear-gradient(180deg,var(--sky-top) 0,var(--sky-mid) 300px,var(--sky-low) 520px,var(--white) 600px);
  }
  .sky-rays{
    position:absolute;left:0;top:0;width:1200px;height:600px;
    background:radial-gradient(ellipse at 560px 40px,rgba(255,255,255,.55) 0,rgba(255,255,255,0) 420px);
  }
  .sky-clouds{
    position:absolute;left:0;top:380px;width:1200px;height:200px;
    background:linear-gradient(180deg,rgba(255,255,255,0),rgba(255,255,255,.8));
  }

  /* header */
  .brand{
    position:absolute;left:168px;top:38px;
    font-weight:700;font-size:36px;letter-spacing:1px;color:var(--brand-blue);
  }
  .main-nav{position:absolute;left:512px;top:17px;height:34px;display:flex;align-items:center;font-size:13px;font-weight:600}
  .main-nav a{color:#111;text-decoration:none}
  .main-nav .current{
    display:inline-block;width:81px;height:33px;line-height:31px;text-align:center;
    border:2px solid #fff;border-radius:7px;background:linear-gradient(180deg,#f4f8fb,#c9d8e3);
    box-shadow:0 1px 3px rgba(0,0,0,.25);
  }
  .main-nav .sep{margin:0 28px;font-weight:400;color:#111}
  .auth{position:absolute;top:88px;display:flex;gap:7px;left:888px}
  .auth a{
    height:27px;line-height:25px;padding:0 14px;border:2px solid #fff;border-radius:6px;
    background:linear-gradient(180deg,#fafafa,#dcdcdc);box-shadow:0 1px 3px rgba(0,0,0,.25);
    font-size:13px;font-weight:600;color:#555;text-decoration:none;
  }

  /* main frame */
  .frame{
    position:absolute;left:132px;top:137px;width:934px;height:600px;
    background:var(--white);border:1px solid var(--panel-border);
  }
  .frame-shadow{position:absolute;left:155px;top:745px;width:900px;height:12px;border-radius:50%;
    background:radial-gradient(ellipse,rgba(0,0,0,.22),rgba(0,0,0,0) 70%)}

  /* sidebar */
  .sidebar{
    position:absolute;left:137px;top:142px;width:193px;height:511px;border-radius:10px;
    background:linear-gradient(180deg,var(--side-top),#0a80c8 280px,var(--side-bottom));
    color:#fff;
  }
  .sidebar-shadow{position:absolute;left:140px;top:652px;width:180px;height:14px;border-radius:50%;
    background:radial-gradient(ellipse,rgba(0,0,0,.28),rgba(0,0,0,0) 70%)}
  .avatar{position:absolute;left:7px;top:12px;width:62px;height:62px;border:3px solid #fff;
    background:linear-gradient(160deg,#8a7766,#3a2f28)}
  .user{position:absolute;left:76px;top:14px;font-size:12px;line-height:18px}
  .user strong{font-weight:700}
  .side-menu{position:absolute;left:0;top:101px;width:193px;list-style:none}
  .side-menu::before{content:"";position:absolute;left:9px;top:0;width:171px;border-top:1px dotted rgba(255,255,255,.5)}
  .side-menu li{
    position:relative;height:34.5px;line-height:34px;padding-left:15px;margin-left:9px;width:171px;
    font-family:"Arimo",sans-serif;font-size:12.5px;letter-spacing:.5px;
    border-bottom:1px dotted rgba(255,255,255,.55);
  }
  .side-menu li::before{content:"";position:absolute;left:0;top:15px;width:5px;height:5px;background:#fff}
  .side-menu li.active{margin-left:0;padding-left:24px;width:173px;color:#333;border-bottom:none;
    background:linear-gradient(180deg,#fff,#e3e3e3);clip-path:polygon(0 0,150px 0,100% 100%,0 100%);height:26px;line-height:26px;margin-top:7px;margin-bottom:2px}
  .side-menu li.active::before{background:#888;left:9px;top:10px}

  /* center column */
  .column-center{position:absolute;left:345px;top:170px;width:470px;height:550px;
    box-shadow:-6px 0 6px -6px rgba(0,0,0,.15),6px 0 6px -6px rgba(0,0,0,.15)}
  .section-title{position:absolute;left:13px;top:-2px;font-size:13.5px;color:#555}
  .section-title::before{content:"";display:inline-block;border-left:5px solid #666;border-top:4px solid transparent;border-bottom:4px solid transparent;margin-right:6px}
  .survey{
    position:absolute;left:8px;width:447px;height:142px;border:1px solid var(--card-border);border-radius:8px;
    background:var(--card-bg);overflow:hidden;
  }
  .survey-head{height:27px;line-height:27px;padding-left:8px;background:linear-gradient(180deg,#fff,#e4e4e4);border-bottom:1px dotted #bbb}
  .survey-head h3{display:inline;font-weight:400;font-size:15px;color:var(--brand-blue)}
  .survey-head span{font-size:12px;color:#555}
  .survey-head svg{position:absolute;right:9px;top:4px}
  .survey p{padding:10px 8px 0;font-family:"Arimo",sans-serif;font-size:11.4px;line-height:17.3px;color:var(--text-body);text-align:justify;letter-spacing:.5px}
  .survey p b{color:#333;letter-spacing:.2px}
  .divider{position:absolute;left:18px;width:430px;border-top:1px dotted #bbb}

  /* right column */
  .search{position:absolute;left:865px;top:150px;width:192px;height:34px;border:2px solid #e4e4e4;border-radius:17px;background:#fff}
  .search button{position:absolute;right:3px;top:4px;width:62px;height:23px;border:none;border-radius:12px;
    background:linear-gradient(180deg,#1ea6e4,#0772ba);color:#fff;font-family:"Source Sans 3",sans-serif;font-weight:700;font-size:12px}
  .widget{position:absolute;left:826px;top:206px;width:232px;height:263px;border:1px solid #e4e4e4;border-radius:10px;
    background:linear-gradient(180deg,#fafafa,#ececec)}
  .widget-shadow{position:absolute;left:850px;top:466px;width:200px;height:12px;border-radius:50%;
    background:radial-gradient(ellipse,rgba(0,0,0,.25),rgba(0,0,0,0) 70%)}
  .widget h2{height:39px;line-height:38px;padding-left:17px;font-size:18px;font-weight:400;color:var(--brand-blue);
    background:#fff;border-radius:10px 10px 0 0;border-bottom:1px solid #e8e8e8}
  .widget h2 b{font-weight:700}
  .select{position:absolute;left:10px;top:54px;width:206px;height:27px;border:1px solid #ccc;background:#fff;font-size:13.5px;line-height:25px;padding-left:8px}
  .select i{position:absolute;right:5px;top:5px;width:15px;height:15px;border:1px solid #777;background:#eee}
  .select i::after{content:"";position:absolute;left:3px;top:5px;border-top:5px solid #333;border-left:4px solid transparent;border-right:4px solid transparent}
  .field{position:absolute;left:18px;font-size:12px;color:#555;display:flex;align-items:center}
  .field label{width:54px}
  .field .box{width:97px;height:24px;border:1px solid #d6d6d6;border-radius:7px;background:#fff;margin-left:6px;padding-left:8px;line-height:22px;color:#333}
  .field .unit{margin-left:8px}
  .submit{position:absolute;left:128px;top:216px;width:85px;height:32px;border-radius:16px;
    background:linear-gradient(180deg,var(--submit-top),var(--submit-bottom));color:#fff;font-size:16px;text-align:center;line-height:32px}

  /* footer */
  .footer{position:absolute;left:0;top:804px;width:1200px;height:60px;background:linear-gradient(180deg,var(--footer-top),var(--footer-bottom))}
  .footer-nav{position:absolute;left:331px;top:21px;font-size:13px;color:#fff;white-space:nowrap}
  .footer-nav .sep{margin:0 14px;color:#fff}
  .social{position:absolute;top:14px;width:33px;height:33px;border-radius:50%;background:linear-gradient(180deg,#9a9a9a,#555);border:1px solid #aaa}
</style>
</head>
<body>
  <div class="sky-rays"></div>
  <div class="sky-clouds" role="img" aria-label="Soft clouds in a blue sky"></div>

  <header>
    <div class="brand">vornatik</div>
    <nav class="main-nav">
      <a class="current" href="#">About us</a><span class="sep">|</span>
      <a href="#">solutions</a><span class="sep">|</span>
      <a href="#">Services</a><span class="sep">|</span>
      <a href="#">News &amp; Events</a><span class="sep">|</span>
      <a href="#">Contact us</a>
    </nav>
    <div class="auth"><a href="#">Login</a><a href="#">Sign Up Now</a></div>
  </header>

  <div class="frame-shadow"></div>
  <main class="frame"></main>

  <div class="sidebar-shadow"></div>
  <aside class="sidebar">
    <div class="avatar" role="img" aria-label="Profile photo of the signed-in user"></div>
    <div class="user"><strong>Marco Ellery</strong><br>Last Login: 16 January<br>2012</div>
    <ul class="side-menu">
      <li class="active">HOME</li>
      <li>PATIENTS</li>
      <li>PROFESSIONALS</li>
      <li>STUDIES</li>
      <li>SURVEYS</li>
      <li>DESIGNER</li>
    </ul>
  </aside>

  <section class="column-center">
    <div class="section-title">Available Surveys</div>

    <article class="survey" style="top:25px">
      <div class="survey-head"><h3>Lower Extemity functional</h3> <span>Scale by Marco Ellery</span>
        <svg width="24" height="19" viewBox="0 0 24 19"><rect x="7" y="1" width="16" height="10" rx="3" fill="#9aa5ad"/><rect x="1" y="6" width="16" height="10" rx="3" fill="#2aa6e0"/><path d="M4 15 l0 4 l4 -4z" fill="#2aa6e0"/></svg></div>
      <p><b>Lorem Ipsum is simply dummy text of the printing and typesetting industry. Lorem Ipsum has been the</b> industry's standard dummy text ever since the 1500s, when an unknown printer took a galley of type and scrambled it to make a type specimen book. It has survived not only five centuries, but also the leap into electronic typesetting,</p>
    </article>
    <div class="divider" style="top:176px"></div>

    <article class="survey" style="top:185px">
      <div class="survey-head"><h3>Lower Extemity functional</h3> <span>Scale by Marco Ellery</span>
        <svg width="24" height="19" viewBox="0 0 24 19"><rect x="7" y="1" width="16" height="10" rx="3" fill="#9aa5ad"/><rect x="1" y="6" width="16" height="10" rx="3" fill="#2aa6e0"/><path d="M4 15 l0 4 l4 -4z" fill="#2aa6e0"/></svg></div>
      <p><b>Lorem Ipsum is simply dummy text of the printing and typesetting industry. Lorem Ipsum has been the</b> industry's standard dummy text ever since the 1500s, when an unknown printer took a galley of type and scrambled it to make a type specimen book. It has survived not only five centuries, but also the leap into electronic typesetting,</p>
    </article>
    <div class="divider" style="top:335px"></div>

    <article class="survey" style="top:344px">
      <div class="survey-head"><h3>Lower Extemity functional</h3> <span>Scale by Marco Ellery</span>
        <svg width="24" height="19" viewBox="0 0 24 19"><rect x="7" y="1" width="16" height="10" rx="3" fill="#9aa5ad"/><rect x="1" y="6" width="16" height="10" rx="3" fill="#2aa6e0"/><path d="M4 15 l0 4 l4 -4z" fill="#2aa6e0"/></svg></div>
      <p><b>Lorem Ipsum is simply dummy text of the printing and typesetting industry. Lorem Ipsum has been the</b> industry's standard dummy text ever since the 1500s, when an unknown printer took a galley of type and scrambled it to make a type specimen book. It has survived not only five centuries, but also the leap into electronic typesetting,</p>
    </article>
  </section>

  <div class="search">
    <svg style="position:absolute;left:6px;top:7px" width="22" height="22" viewBox="0 0 22 22"><circle cx="9" cy="9" r="6.5" fill="none" stroke="#b8c2c8" stroke-width="2"/><path d="M14 14 l6 6" stroke="#b8c2c8" stroke-width="3" stroke-linecap="round"/></svg>
    <button>Search</button>
  </div>

  <div class="widget-shadow"></div>
  <section class="widget">
    <h2>My Daily <b>numbers</b></h2>
    <div class="select">Blood Pressure<i></i></div>
    <div class="field" style="top:114px"><label>Diastolic :</label><span class="box"></span><span class="unit">mmHg</span></div>
    <div class="field" style="top:149px"><label>Systolic &nbsp;&nbsp;:</label><span class="box"></span><span class="unit">mmHg</span></div>
    <div class="field" style="top:184px"><label>Date &nbsp;&nbsp;&nbsp;&nbsp;&nbsp;&nbsp;:</label><span class="box">01/16/2012</span></div>
    <div class="submit">Submit</div>
  </section>

  <footer class="footer">
    <nav class="footer-nav">About us <span class="sep" style="margin-left:4px">|</span>Products &amp; solutions<span class="sep">|</span>Services<span class="sep">|</span>News &amp; Events<span class="sep">|</span>Regulatory &amp; Scientific</nav>
    <span class="social" style="left:992px"></span>
    <span class="social" style="left:1031px"></span>
  </footer>
</body>
</html>
```